Re-Design my old Business Card

We need a new business card design. The current layout is lacking good design.
We manufacture building products and also offers services (www.tormavestructures.com.au)
I've attached the old business card to show you what we don't want.
I've also attached the new logo in two styles for you to chose from.
The final design should communicate smarter building design and lifestyle, with a clean and crisp designed card.

Target Market(s)

Architects, building companies

Industry/Entity Type

Business

Contact Information for Business Card

See attached old business cards for all details to include

Font styles to use
Sans Serif

Colors
9bcb3b

Requirements
Must have
• Clean crisp look
Nice to have
• Totally up to you

```html
<!DOCTYPE html>
<html lang="en">
<head>
<meta charset="utf-8">
<title>Tormave Structures – Business Card</title>
<link rel="stylesheet" href="https://fonts.googleapis.com/css2?family=Open+Sans:wght@400;600;700&display=swap">
<style>
  :root {
    --brand-green: #8dc03f;
    --deep-green: #3d6a1c;
    --ink-green: #2f5a14;
    --card-white: #ffffff;
    --backdrop: #f1f3ee;
    --edge: #dfe4d8;
  }
  * { box-sizing: border-box; margin: 0; padding: 0; }
  html, body {
    width: 1200px;
    height: 1182px;
    overflow: hidden;
    background: var(--backdrop);
    font-family: "Open Sans", Arial, sans-serif;
  }
  .sheet {
    position: relative;
    width: 1200px;
    height: 1182px;
  }
  .card {
    position: absolute;
    left: 150px;
    width: 900px;
    height: 500px;
    background: var(--card-white);
    border: 1px solid var(--edge);
    overflow: hidden;
  }
  .card--front { top: 60px; }
  .card--back  { top: 622px; }
  .card__band {
    position: absolute;
    left: 0;
    right: 0;
    bottom: 6px;
    height: 12px;
    background: var(--brand-green);
  }

  /* brand name block */
  .brand {
    position: absolute;
    display: flex;
    align-items: center;
    gap: 16px;
    color: var(--brand-green);
    font-weight: 600;
    letter-spacing: 0.02em;
    text-transform: uppercase;
    white-space: nowrap;
  }
  .brand__square {
    background: var(--brand-green);
    flex: none;
  }
  .brand--front {
    left: 92px;
    top: 92px;
    font-size: 32px;
  }
  .brand--front .brand__square { width: 38px; height: 38px; }
  .brand--back {
    left: 0;
    right: 0;
    top: 214px;
    justify-content: center;
    font-size: 44px;
  }
  .brand--back .brand__square { width: 52px; height: 52px; }

  /* person */
  .person {
    position: absolute;
    left: 130px;
    top: 262px;
    color: var(--deep-green);
    white-space: nowrap;
  }
  .person__name {
    font-size: 31px;
    font-weight: 700;
    letter-spacing: 0.03em;
    text-transform: uppercase;
    line-height: 1.2;
  }
  .person__role {
    margin-top: 4px;
    margin-left: 10px;
    font-size: 14px;
    font-weight: 600;
  }

  /* contact column */
  .contact {
    position: absolute;
    left: 592px;
    top: 178px;
    color: var(--ink-green);
    font-size: 13.5px;
    font-weight: 600;
    line-height: 1.35;
    font-style: normal;
    white-space: nowrap;
  }
  .contact__office { margin-bottom: 14px; }
  .contact__phones {
    list-style: none;
    margin-left: 12px;
    margin-bottom: 12px;
    line-height: 1.6;
  }
  .contact__label {
    display: inline-block;
    width: 22px;
  }
  .contact__sep {
    display: inline-block;
    width: 18px;
  }
  .contact__web { margin-left: 20px; line-height: 1.75; }

  .card__mark {
    position: absolute;
    left: 440px;
    bottom: 30px;
    width: 22px;
    height: 22px;
    background: var(--brand-green);
  }
</style>
</head>
<body>
<main class="sheet">

  <section class="card card--front" aria-label="Business card front">
    <div class="brand brand--front">
      <span class="brand__square"></span>
      <span class="brand__name">Tormave Structures</span>
    </div>

    <div class="person">
      <h1 class="person__name">Darren Kellow</h1>
      <p class="person__role">Account Manager Qld / Northern NSW</p>
    </div>

    <address class="contact">
      <p class="contact__office">Head Office<br>Unit 4/27 Harlow Road<br>Brenfield, QLD 4172</p>
      <ul class="contact__phones">
        <li><span class="contact__label">M</span><span class="contact__sep">:</span>0491 620 357</li>
        <li><span class="contact__label">P</span><span class="contact__sep">:</span>1300 472 190</li>
        <li><span class="contact__label">F</span><span class="contact__sep">:</span>1300 472 191</li>
      </ul>
      <p class="contact__web">darren@tormavestructures.com.au<br>www.tormavestructures.com.au</p>
    </address>

    <span class="card__mark"></span>
    <span class="card__band"></span>
  </section>

  <section class="card card--back" aria-label="Business card back">
    <div class="brand brand--back">
      <span class="brand__square"></span>
      <span class="brand__name">Tormave Structures</span>
    </div>
    <span class="card__band"></span>
  </section>

</main>
</body>
</html>
```